I need an amazing business card!

I am the principle in my own software company that develops zelPad and mobile applications. I require a great business card design. I've attached my corporate logo (Thanks Teodor!).
I would like the design to integrate the logo, my name, email address and skype account:
name Brent Halvorsen
email brenthalvorsen@tvekra.com
skype brenthalvorsen.net
I would like the back of the card to have a "write on me area" similar to the "write on me" card on this page, row 6:
http://us.plinkora.com/design-templates/business-cards/#industry=Computing%20%26%20IT
As far as the rest - it's all you!
Updates
1) Please add an example telephone number as well.
Industry/Entity Type
Software
Look and feel
Each slider illustrates characteristics of the customer's brand and the style your logo design should communicate.

```html
<!DOCTYPE html>
<html lang="en">
<head>
<meta charset="utf-8">
<title>Tvekra — Business Card</title>
<link rel="stylesheet" href="https://fonts.googleapis.com/css2?family=Lato:ital,wght@0,300;0,400;0,700;1,400&display=swap">
<style>
  :root {
    --green: #9cc03c;
    --green-light: #b3cc4e;
    --green-deep: #8fb533;
    --charcoal: #474747;
    --white: #ffffff;
    --rule: #d9e6b3;
    --backdrop: #e6e6e6;
  }
  * { box-sizing: border-box; margin: 0; padding: 0; }
  html, body {
    width: 1200px; height: 926px; overflow: hidden;
    background: var(--backdrop);
    font-family: "Lato", sans-serif;
  }
  .canvas {
    position: relative; width: 1200px; height: 926px;
    display: flex; flex-direction: column; align-items: center;
    justify-content: center; gap: 42px;
  }
  .card {
    position: relative; width: 700px; height: 400px; overflow: hidden;
    box-shadow: 0 6px 18px rgba(0,0,0,0.18);
  }

  /* Front */
  .card-front { background: var(--white); }
  .front-top {
    position: absolute; left: 0; top: 0; width: 100%; height: 168px;
    display: flex; flex-direction: column; align-items: center; justify-content: center;
  }
  .brand { display: flex; flex-direction: column; align-items: center; gap: 10px; }
  .brand-square {
    width: 72px; height: 72px; border-radius: 14px; background: var(--green);
  }
  .brand-name {
    font-weight: 400; font-size: 22px; letter-spacing: 12px;
    color: var(--green); margin-right: -12px;
  }
  .front-stripe {
    position: absolute; left: 0; top: 168px; width: 100%; height: 12px;
    background: var(--green);
  }
  .front-bottom {
    position: absolute; left: 0; top: 180px; width: 100%; bottom: 0;
    background: var(--charcoal);
    display: flex; flex-direction: column; align-items: center; padding-top: 48px;
  }
  .person-name {
    font-size: 40px; letter-spacing: 1px; color: var(--green);
    text-transform: uppercase; font-weight: 400;
  }
  .person-name strong { font-weight: 700; }
  .contact { margin-top: 16px; font-size: 20px; line-height: 1.35; color: var(--white); }
  .contact-row { display: flex; gap: 8px; }
  .contact-label {
    width: 74px; text-align: right; font-style: italic; color: var(--green);
  }

  /* Back */
  .card-back {
    background: linear-gradient(180deg, var(--green-light) 0%, var(--green-deep) 100%);
  }
  .back-brand {
    position: absolute; left: 0; top: 30px; width: 100%;
    display: flex; flex-direction: column; align-items: center; gap: 10px;
  }
  .back-brand .brand-square { background: var(--white); width: 64px; height: 64px; }
  .back-brand .brand-name { color: var(--white); font-size: 20px; }
  .write-area {
    position: absolute; left: 56px; right: 56px; top: 172px; height: 188px;
    background: var(--white);
  }
  .write-area svg { display: block; width: 100%; height: 100%; }
</style>
</head>
<body>
<main class="canvas">
  <section class="card card-front" aria-label="Card front">
    <div class="front-top">
      <div class="brand">
        <span class="brand-square" aria-hidden="true"></span>
        <span class="brand-name">tvekra</span>
      </div>
    </div>
    <div class="front-stripe"></div>
    <div class="front-bottom">
      <h1 class="person-name">Brent <strong>Halvorsen</strong></h1>
      <div class="contact">
        <p class="contact-row"><span class="contact-label">email:</span><span>brenthalvorsen@tvekra.com</span></p>
        <p class="contact-row"><span class="contact-label">skype:</span><span>brenthalvorsen.net</span></p>
      </div>
    </div>
  </section>

  <section class="card card-back" aria-label="Card back">
    <div class="back-brand">
      <span class="brand-square" aria-hidden="true"></span>
      <span class="brand-name">tvekra</span>
    </div>
    <div class="write-area">
      <svg viewBox="0 0 588 188" preserveAspectRatio="none" aria-label="Write-on area">
        <line x1="36" y1="40" x2="552" y2="40" stroke="var(--rule)" stroke-width="2"/>
        <line x1="36" y1="88" x2="552" y2="88" stroke="var(--rule)" stroke-width="2"/>
        <line x1="36" y1="136" x2="552" y2="136" stroke="var(--rule)" stroke-width="2"/>
      </svg>
    </div>
  </section>
</main>
</body>
</html>
```